Brand Business Card for Hotel Cloud Management System

Hello designers,
we are looking for a new brand business card for our product Stayvora. Our brand Stayvora is a hotel management system for small hotels, B&B, guesthouses etc. and just recently we are expanding our offer to other European markets. Therefore we need a business card that will communicate not only to the end-users (hoteliers) but also to potential business partners/ We would like the brand business card to be professional looking, but not too serius, modern, elegant, clean, Our brand color is orange, dark grey and it would be nice to see both combined.

Please visit our website www.stayvora.eu to get more impression on what our brand stayvora stands for.

Please find attached stayvora logo.

Target Market(s)

small hotels, hoteliers, B&B owners, potential business partners

Industry/Entity Type

Software Service

Contact Information for Business Card

Stayvora
- hotel software solutions - web booking engine - multi channel manager
www.stayvora.eu
T: +38614738265
E: info@stayvora.net

Font styles to use
Serif
Sans Serif

Colors
f37122
aaaaaa
606060
f6f6f6

Requirements
Must have
• Logo of the brand
• the layout of the business card should be in connection with the look and feel of the website stayvora.eu and logo stayvora;

```html
<!DOCTYPE html>
<html lang="en">
<head>
<meta charset="utf-8">
<title>Stayvora – Business Card</title>
<link rel="stylesheet" href="https://fonts.googleapis.com/css2?family=Quicksand:wght@500;700&display=swap">
<style>
  :root {
    --brand-orange: #f37122;
    --ink-dark: #1f1f1f;
    --ink-grey: #606060;
    --paper: #ffffff;
    --backdrop: #3d3e3d;
  }
  * { margin: 0; padding: 0; box-sizing: border-box; }
  html, body { width: 1200px; height: 1200px; overflow: hidden; }
  body {
    background: var(--backdrop);
    font-family: "Quicksand", sans-serif;
    position: relative;
  }
  .card {
    position: absolute;
    left: 208px;
    width: 811px;
    height: 452px;
    overflow: hidden;
  }
  .card--front { top: 152px; background: var(--paper); }
  .card--back { top: 621px; background: var(--brand-orange); }

  .card__pattern { position: absolute; inset: 0; width: 100%; height: 100%; }

  .brand {
    position: absolute;
    left: 32px;
    top: 62px;
    display: flex;
    flex-direction: column;
  }
  .brand__row { display: flex; align-items: center; gap: 12px; }
  .brand__name {
    font-weight: 700;
    font-size: 56px;
    line-height: 1;
    letter-spacing: -1px;
    color: var(--ink-dark);
  }
  .brand__mark {
    width: 16px; height: 16px;
    background: var(--brand-orange);
  }
  .card--back .brand__mark { background: var(--paper); }
  .brand__tagline {
    margin-top: 4px;
    font-weight: 500;
    font-size: 18px;
    color: var(--ink-dark);
  }

  .contact {
    position: absolute;
    left: 32px;
    top: 338px;
    list-style: none;
  }
  .contact__item {
    display: flex;
    align-items: center;
    gap: 8px;
    height: 28.5px;
    font-weight: 500;
    font-size: 24px;
    color: var(--ink-grey);
  }
  .card--back .contact__item { color: var(--ink-dark); }
  .contact__icon { width: 19px; height: 19px; flex: none; }
  .contact__icon .disc { fill: var(--brand-orange); }
  .card--back .contact__icon .disc { fill: var(--paper); }
  .contact__icon .glyph { fill: none; stroke: var(--paper); stroke-width: 1.3; }
  .card--back .contact__icon .glyph { stroke: var(--brand-orange); }
</style>
</head>
<body>

<section class="card card--front">
  <svg class="card__pattern" viewBox="0 0 811 452" role="img" aria-label="Decorative band with repeating product tagline pattern">
    <path d="M368 452 L610 210 Q640 180 680 178 L811 170 L811 452 Z" fill="var(--brand-orange)"/>
  </svg>
  <div class="brand">
    <div class="brand__row">
      <span class="brand__name">Stayvora</span>
      <span class="brand__mark"></span>
    </div>
    <span class="brand__tagline">hotel pms service</span>
  </div>
  <ul class="contact">
    <li class="contact__item">
      <svg class="contact__icon" viewBox="0 0 20 20"><circle class="disc" cx="10" cy="10" r="10"/><g class="glyph"><circle cx="10" cy="10" r="5.5"/><ellipse cx="10" cy="10" rx="2.4" ry="5.5"/><path d="M4.5 10h11"/></g></svg>
      www.stayvora.eu
    </li>
    <li class="contact__item">
      <svg class="contact__icon" viewBox="0 0 20 20"><circle class="disc" cx="10" cy="10" r="10"/><path class="glyph" d="M6.5 5.5c0 5 3 8 8 8l0-2.2-2.2-.8-1 1c-1.5-.6-2.6-1.7-3.2-3.2l1-1-.8-2.2z"/></svg>
      +38614738265
    </li>
    <li class="contact__item">
      <svg class="contact__icon" viewBox="0 0 20 20"><circle class="disc" cx="10" cy="10" r="10"/><g class="glyph"><rect x="5" y="6.5" width="10" height="7"/><path d="M5 6.5l5 4 5-4"/></g></svg>
      info@stayvora.net
    </li>
  </ul>
</section>

<section class="card card--back">
  <svg class="card__pattern" viewBox="0 0 811 452" role="img" aria-label="Decorative band with repeating product tagline pattern">
    <path d="M360 0 L755 0 L650 240 Q632 280 590 262 L345 160 Q320 148 325 120 Z" fill="var(--paper)"/>
  </svg>
  <div class="brand">
    <div class="brand__row">
      <span class="brand__name">Stayvora</span>
      <span class="brand__mark"></span>
    </div>
    <span class="brand__tagline">hotel pms service</span>
  </div>
  <ul class="contact">
    <li class="contact__item">
      <svg class="contact__icon" viewBox="0 0 20 20"><circle class="disc" cx="10" cy="10" r="10"/><g class="glyph"><circle cx="10" cy="10" r="5.5"/><ellipse cx="10" cy="10" rx="2.4" ry="5.5"/><path d="M4.5 10h11"/></g></svg>
      www.stayvora.eu
    </li>
    <li class="contact__item">
      <svg class="contact__icon" viewBox="0 0 20 20"><circle class="disc" cx="10" cy="10" r="10"/><path class="glyph" d="M6.5 5.5c0 5 3 8 8 8l0-2.2-2.2-.8-1 1c-1.5-.6-2.6-1.700-3.2-3.2l1-1-.8-2.2z"/></svg>
      +38614738265
    </li>
    <li class="contact__item">
      <svg class="contact__icon" viewBox="0 0 20 20"><circle class="disc" cx="10" cy="10" r="10"/><g class="glyph"><rect x="5" y="6.5" width="10" height="7"/><path d="M5 6.5l5 4 5-4"/></g></svg>
      info@stayvora.net
    </li>
  </ul>
</section>

</body>
</html>
```